Wordpress Theme for a Professional Speaker's Website

I I need a website to promote myself as a speaker to corporations and meeting planners. Some examples of similar sites I like are:

http://www.beginwithpurpose-demo.net (this is by far my favorite)
http://www.lorapemberton.net
http://www.teddyvance.net
http://www.bolsinter.net
http://www.dawnacrossridges.net
http://www.rudyfallenbrook.net

I like modern, minimalistic, innovative. I'm okay if it's edgy but still want it communicate professionalism.

The primary objective is to position me as an expert who can deliver valuable information in an entertaining manner.

There are two calls to action. The first is to capture name and email address to subscribe to my newsletter. The second is to request more information about booking me to speak for their company, organization, etc.

The pages on the website will ultimately be the following:

1. Home (should include sections for recent blog posts, featured topics/presentations, short bio, testimonials, email capture, and anything else you think should be added.
2. Meet Owen
3. Blog
4. Keynotes & Speaking
5. Training & Webinars
6. Coaching & Consulting
7. Testimonials
8. Book Owen
9. Media Inquiries
10. Contact

Please feel free to use your creativity. I don't want my requirements to limit you in any way. I'm just looking for a modern, professional site that will make me stand out from the crowd.

I don't have any existing site or brand identity. My plan is to have the website design I ultimately choose serve as the foundation for the rest of my brand identity.

Target Market(s)

Corporate meeting planners and executives

Industry/Entity Type

It Professional

Font styles to use
Sans Serif

Requirements
Must have
• Email capture, testimonials, blog
Nice to have
• None
Should not have
• None

```html
<!DOCTYPE html>
<html lang="en">
<head>
<meta charset="utf-8">
<title>Owen Castell – Speaker</title>
<link rel="stylesheet" href="https://fonts.googleapis.com/css2?family=Raleway:ital,wght@0,500;0,600;0,700;1,500&family=Lato:wght@400;700&display=swap">
<style>
:root{
  --green:#79b531;
  --green-dark:#669c26;
  --ink:#1e1e1e;
  --text:#333;
  --muted:#666;
  --light:#efefef;
  --card:#f3f3f3;
  --line:#d8d8d8;
  --dark:#2d2d2d;
  --white:#fff;
}
*{margin:0;padding:0;box-sizing:border-box}
html,body{width:1200px;height:3243px;overflow:hidden}
body{position:relative;background:var(--white);font-family:"Lato",sans-serif;color:var(--text)}
.abs{position:absolute}
h2,.heading{font-family:"Raleway",sans-serif;font-weight:700;color:var(--ink)}
.accent{color:var(--green)}
.btn{position:absolute;background:var(--green);color:var(--white);font-family:"Raleway",sans-serif;font-weight:700;font-size:13px;display:flex;align-items:center;justify-content:center;border-bottom:3px solid var(--green-dark)}
.photo{position:absolute}

/* top bar */
.topbar{left:238px;top:0;width:962px;height:30px;background:var(--green);clip-path:polygon(28px 0,100% 0,100% 100%,0 100%)}
.topbar-links{left:310px;top:0;height:30px;display:flex;gap:54px;align-items:center;font-family:"Raleway",sans-serif;font-weight:700;font-size:13.5px;color:var(--white)}
.search{left:930px;top:4px;width:173px;height:22px;background:var(--white);font-size:11px;color:#777;padding:5px 8px}
.search svg{position:absolute;right:6px;top:4px}

/* header */
.logo{left:97px;top:58px;font-family:"Raleway",sans-serif;font-weight:700;font-size:35px;color:var(--ink)}
.logo span{color:var(--green)}
.nav{left:420px;top:56px;display:flex;align-items:center;font-family:"Raleway",sans-serif;font-weight:700;font-size:13.5px;color:var(--ink)}
.nav a{display:block;padding:0 26px;height:65px;line-height:65px;text-decoration:none;color:inherit}
.nav a.active{background:var(--green);color:var(--white);padding:0 24px;line-height:38px;height:65px}

/* hero */
.hero{left:0;top:117px;width:1200px;height:467px;background:radial-gradient(ellipse at 30% 55%,#7a4a32 0%,#4a2c20 45%,#2a1d18 100%)}
.hero-caption{right:112px;top:296px;text-align:right;font-family:"Raleway",sans-serif;font-weight:600;font-size:30px;line-height:42px;color:var(--white)}
.hero-caption span{background:rgba(0,0,0,.45);padding:2px 8px}
.arrow{top:333px;width:28px;height:28px;background:#111;display:flex;align-items:center;justify-content:center}

/* newsletter */
.newsletter{left:100px;top:547px;width:1003px;height:102px;background:var(--white);box-shadow:0 6px 8px rgba(0,0,0,.12)}
.newsletter-title{left:100px;top:547px;width:368px;height:102px;background:var(--green);clip-path:polygon(0 0,100% 0,88% 100%,0 100%);display:flex;align-items:center;padding-left:24px;font-family:"Raleway",sans-serif;font-weight:700;font-size:29px;color:var(--white)}
.field{top:580px;height:34px;border:1px solid var(--line);font-size:11px;color:#444;padding:10px 10px}

/* featured */
.featured-label{left:100px;top:690px;font-family:"Raleway",sans-serif;font-weight:700;font-size:29px;color:var(--ink)}
.brand{top:681px;width:151px;height:63px;border:1px solid #bbb;display:flex;align-items:center;justify-content:center;font-family:"Lato",sans-serif;font-weight:700;font-size:21px;color:#333}

/* section titles */
.section-title{left:0;width:1200px;text-align:center;font-size:30px}
.rule{height:2px;background:var(--line);left:380px;width:440px}
.rule::after{content:"";position:absolute;left:192px;top:-1px;width:56px;height:4px;background:var(--green)}

/* keynotes */
.keynotes{left:0;top:778px;width:1200px;height:372px;background:var(--light)}
.topic{top:912px;width:270px;text-align:center}
.topic .circle{width:122px;height:122px;border-radius:50%;background:var(--green);margin:0 auto;display:flex;align-items:center;justify-content:center}
.topic h3{font-family:"Raleway",sans-serif;font-weight:700;font-size:17px;color:var(--ink);margin-top:14px}
.topic p{font-size:13px;line-height:20px;color:#444;margin-top:4px}

/* about */
.about-title{left:100px;top:1186px;font-size:30px}
.about-line{left:100px;top:1243px;width:765px;height:1px;background:var(--line)}
.about-text{left:100px;top:1272px;width:765px;font-size:13px;line-height:23.5px;color:#444}
.follow{left:227px;top:1464px;font-size:12.5px;color:#333}
.social{top:1462px;width:21px;height:21px;background:#3a3a3a}

/* video */
.video-band{left:0;top:1535px;width:1200px;height:188px;background:linear-gradient(90deg,#2b2b2b,#3c3a38 50%,#2b2b2b)}
.video-quote{left:0;top:1556px;width:1200px;text-align:center;font-family:"Raleway",sans-serif;font-style:italic;font-weight:500;font-size:24px;color:var(--white)}
.video-frame{left:117px;top:1606px;width:516px;height:411px;background:linear-gradient(160deg,#6f7a80,#3b3f42 55%,#1f2123)}
.play{left:335px;top:1773px;width:86px;height:86px;border-radius:50%;background:var(--white);display:flex;align-items:center;justify-content:center}
.video-card{left:584px;top:1675px;width:501px;height:314px;background:var(--card);box-shadow:0 2px 6px rgba(0,0,0,.1)}
.video-card h2{position:absolute;left:30px;top:26px;font-size:30px}
.video-card .line{position:absolute;left:30px;top:80px;width:440px;height:1px;background:var(--line)}
.video-card p{position:absolute;left:30px;top:104px;width:445px;font-size:12.8px;line-height:23.5px;color:#444}

/* blog */
.post{top:2147px;width:318px}
.post .thumb{width:318px;height:173px}
.post .date{position:absolute;left:0;top:0;width:47px;height:102px;background:var(--green);color:var(--white);text-align:center;font-size:13px;line-height:17px;padding-top:8px}
.post .date b{display:block;font-weight:400;font-size:14px}
.post h3{font-family:"Raleway",sans-serif;font-weight:700;font-size:15px;color:var(--ink);margin-top:32px}
.post p{font-size:12px;line-height:21px;color:#444;margin-top:12px;width:300px}
.post .meta{border-top:1px solid var(--line);border-bottom:1px solid var(--line);margin-top:18px;padding:8px 0;font-size:12px;color:#444;display:flex}
.post .meta span{padding-right:14px}
.post .meta span+span{border-left:1px solid var(--line);padding-left:14px}

/* testimonials */
.testimonials{left:0;top:2536px;width:1200px;height:443px;background:var(--light)}
.quote-text{left:233px;top:2662px;width:740px;text-align:center;font-size:12.6px;line-height:22px;color:#444}
.qmark{top:2656px;font-family:"Raleway",sans-serif;font-weight:700;font-size:110px;line-height:110px;color:#c9c9c9}
.client-name{left:0;top:2748px;width:1200px;text-align:center;font-family:"Raleway",sans-serif;font-weight:700;font-size:14px;color:var(--green)}
.avatar{border-radius:50%}
.dot{top:2925px;width:22px;height:4px;background:#cfcfcf}

/* footer */
.footer{left:0;top:2979px;width:1200px;height:223px;background:var(--dark);color:var(--white)}
.footer h4{position:absolute;top:36px;font-family:"Raleway",sans-serif;font-weight:700;font-size:14px}
.footer ul{position:absolute;top:80px;list-style:none;font-size:11.5px;line-height:20px}
.footer ul li::before{content:"";display:inline-block;width:4px;height:4px;border-radius:50%;background:var(--white);margin-right:9px;vertical-align:middle}
.footer .divider{position:absolute;top:36px;width:1px;height:160px;background:#444}
.contact-row{position:absolute;left:569px;display:flex;gap:16px;font-size:11.5px;line-height:16px}
.follow-row{position:absolute;left:962px;display:flex;align-items:center;gap:10px;font-size:11.5px}
.follow-row i{display:block;width:20px;height:20px;background:var(--white)}
.copyright{left:0;top:3202px;width:1200px;height:41px;background:var(--green);color:var(--white);text-align:center;line-height:41px;font-size:12.5px}
</style>
</head>
<body>

<!-- top bar -->
<div class="abs topbar"></div>
<div class="abs topbar-links"><span>Training &amp; Webinars</span><span>Coaching &amp; Consulting</span><span>Book Owen</span><span>Media Inquiries</span></div>
<div class="abs search">Search
  <svg width="14" height="14" viewBox="0 0 14 14"><circle cx="6" cy="6" r="4" fill="none" stroke="#79b531" stroke-width="1.6"/><line x1="9" y1="9" x2="13" y2="13" stroke="#79b531" stroke-width="1.6"/></svg>
</div>

<!-- header -->
<div class="abs logo"><span>Owen</span> Castell</div>
<nav class="abs nav">
  <a class="active">Home</a><a>Meet Owen</a><a>Blog</a><a>Keynotes &amp; Speaking</a><a>Testimonials</a><a>Contact</a>
</nav>

<!-- hero -->
<div class="photo hero" role="img" aria-label="Speaker on stage addressing a large seated conference audience"></div>
<div class="abs hero-caption"><span>I am speaker to corporations</span><br><span>and meeting planners</span></div>
<div class="abs arrow" style="left:42px"><svg width="12" height="12" viewBox="0 0 12 12"><path d="M8 1 3 6l5 5" fill="none" stroke="#fff" stroke-width="2"/></svg></div>
<div class="abs arrow" style="left:1128px"><svg width="12" height="12" viewBox="0 0 12 12"><path d="M4 1l5 5-5 5" fill="none" stroke="#fff" stroke-width="2"/></svg></div>

<!-- newsletter -->
<div class="abs newsletter"></div>
<div class="abs newsletter-title">Newsletter&nbsp;<span style="color:#1e1e1e">Signup</span></div>
<div class="abs field" style="left:465px;width:223px">Name</div>
<div class="abs field" style="left:729px;width:222px">Email</div>
<div class="btn" style="left:986px;top:580px;width:95px;height:31px">Subscribe</div>

<!-- featured on -->
<div class="abs featured-label">As <span class="accent">Featured On</span></div>
<div class="abs brand" style="left:357px">Arcwell</div>
<div class="abs brand" style="left:556px">Norvale</div>
<div class="abs brand" style="left:752px">Trenta</div>
<div class="abs brand" style="left:951px">Palisade</div>

<!-- keynotes -->
<div class="abs keynotes"></div>
<h2 class="abs section-title" style="top:812px">Keynotes &amp; <span class="accent">Speaking</span></h2>
<div class="abs rule" style="top:870px"></div>
<div class="abs topic" style="left:51px"><div class="circle"><svg width="60" height="60" viewBox="0 0 60 60" fill="#fff"><circle cx="30" cy="16" r="6"/><rect x="25" y="24" width="10" height="22" rx="3"/><circle cx="14" cy="24" r="5"/><rect x="10" y="31" width="8" height="18" rx="3"/><circle cx="46" cy="24" r="5"/><rect x="42" y="31" width="8" height="18" rx="3"/></svg></div><h3>Leadership</h3><p>Lorem ipsum dolor sit amet,<br>consectetuer adipiscing... [ + ]</p></div>
<div class="abs topic" style="left:325px"><div class="circle"><svg width="60" height="60" viewBox="0 0 60 60"><path d="M8 10h30a4 4 0 0 1 4 4v16a4 4 0 0 1-4 4H20l-8 7v-7H8a4 4 0 0 1-4-4V14a4 4 0 0 1 4-4z" fill="none" stroke="#fff" stroke-width="3"/><path d="M30 24h22a4 4 0 0 1 4 4v14a4 4 0 0 1-4 4h-4v7l-8-7H30a4 4 0 0 1-4-4V28a4 4 0 0 1 4-4z" fill="#fff"/></svg></div><h3>Communication</h3><p>Lorem ipsum dolor sit amet,<br>consectetuer adipiscing... [ + ]</p></div>
<div class="abs topic" style="left:600px"><div class="circle"><svg width="60" height="60" viewBox="0 0 60 60" fill="#fff"><circle cx="30" cy="10" r="6"/><rect x="22" y="18" width="16" height="20" rx="3"/><rect x="23" y="36" width="6" height="20"/><rect x="31" y="36" width="6" height="20"/></svg></div><h3>Entrepreneurism</h3><p>Lorem ipsum dolor sit amet,<br>consectetuer adipiscing... [ + ]</p></div>
<div class="abs topic" style="left:875px"><div class="circle"><svg width="60" height="60" viewBox="0 0 60 60" fill="#fff"><path d="M8 24h10l22-12v34L18 34H8z"/><rect x="14" y="34" width="8" height="14"/><path d="M46 22l8-4M46 29h9M46 36l8 4" stroke="#fff" stroke-width="3"/></svg></div><h3>Marketing</h3><p>Lorem ipsum dolor sit amet,<br>consectetuer adipiscing... [ + ]</p></div>

<!-- about -->
<h2 class="abs about-title">About <span class="accent">Owen</span> Castell</h2>
<div class="abs about-line"></div>
<p class="abs about-text">Lorem ipsum dolor sit amet, consectetuer adipiscing elit, sed diam nonummy nibh euismod tincidunt ut laoreet dolore magna aliquam erat volutpat. Ut wisi enim ad minim veniam, quis nostrud exerci tation ullamcorper suscipit lobortis nisl ut aliquip ex ea commodo consequat. Duis autem vel eum iriure dolor in hendrerit in vulputate velit esse molestie consequat, vel illum dolore eu feugiat nulla facilisis at vero eros et accumsan et iusto odio dignissim qui blandit praesent luptatum zzril delenit augue duis dolore te feugait nulla facilisi.Lorem ipsum dolor sit amet, consectetuer elit, sed diam nonummy nibh euismod tincidunt ut l nostrud exerci tation ullamcorper suscipit lobortis nisl ut aliquip ex ea commodo consequat. Duis autem vel eum iriure dolor in hendrerit in vulputate velit esse</p>
<div class="btn" style="left:100px;top:1459px;width:101px;height:30px">Read More</div>
<div class="abs follow">Follow Us On</div>
<div class="abs social" style="left:329px"></div>
<div class="abs social" style="left:360px"></div>
<div class="abs social" style="left:391px"></div>
<div class="abs social" style="left:422px"></div>
<div class="photo" style="left:886px;top:1189px;width:217px;height:342px;background:linear-gradient(180deg,#e9e6e2,#a79a8a 55%,#6e6557)" role="img" aria-label="Portrait of Owen Castell in a tweed jacket with arms crossed"></div>

<!-- video -->
<div class="photo video-band" role="img" aria-label="Dimmed conference audience backdrop"></div>
<div class="abs video-quote">Lorem ipsum dolor sit amet, consectetuer adipiscing elit, sed diam nonummy nibh</div>
<div class="photo video-frame" role="img" aria-label="Video still of a speaker at a podium"></div>
<div class="abs play"><svg width="28" height="30" viewBox="0 0 28 30"><path d="M4 2l22 13L4 28z" fill="#111"/></svg></div>
<div class="abs video-card">
  <h2>Featured <span class="accent">Video</span></h2>
  <div class="line"></div>
  <p>Lorem ipsum dolor sit amet, consectetuer adipiscing elit, sed diam nonummy nibh euismod tincidunt ut laoreet dolore magna aliquam erat volutpat. Ut wisi enim ad minim veniam, quis nostrud exerci tation ullamcorper suscipit lobortis nisl ut aliquip ex ea commodo consequat. Duis autem vel eum iriure dolor in hendrerit in vulputate ve</p>
</div>
<div class="btn" style="left:614px;top:1918px;width:101px;height:31px">Read More</div>

<!-- blog -->
<h2 class="abs section-title" style="top:2060px">Recent <span class="accent">Blog Posts</span></h2>
<div class="abs rule" style="top:2114px"></div>
<article class="abs post" style="left:100px">
  <div class="thumb" style="background:linear-gradient(150deg,#c65a3a,#5b3b55 60%,#2f3d66)" role="img" aria-label="Speaker facing a conference audience"></div>
  <div class="date">08<b>Aug</b><br>2016</div>
  <h3>Lorem Ipsum Dolor</h3>
  <p>Sed ut perspiciatis unde omnis iste natus errorluptatem accusa nt ium dolorem que laudantium totam rem aperiam laudantium</p>
  <div class="meta"><span><b>By :</b> Sed ut perspiciatis</span><span><b>0</b> Comments</span></div>
</article>
<article class="abs post" style="left:443px">
  <div class="thumb" style="background:linear-gradient(160deg,#f1f1ef,#cfcac2 55%,#7b7874)" role="img" aria-label="Presenter beside a screen in a meeting room"></div>
  <div class="date">08<b>Aug</b><br>2016</div>
  <h3>Lorem Ipsum Dolor</h3>
  <p>Sed ut perspiciatis unde omnis iste natus errorluptatem accusa nt ium dolorem que laudantium totam rem aperiam laudantium</p>
  <div class="meta"><span><b>By :</b> Sed ut perspiciatis</span><span><b>0</b> Comments</span></div>
</article>
<article class="abs post" style="left:783px">
  <div class="thumb" style="background:linear-gradient(150deg,#dfe4e8,#8a9096 50%,#3d4650)" role="img" aria-label="Group of business people listening to a presenter"></div>
  <div class="date">08<b>Aug</b><br>2016</div>
  <h3>Lorem Ipsum Dolor</h3>
  <p>Sed ut perspiciatis unde omnis iste natus errorluptatem accusa nt ium dolorem que laudantium totam rem aperiam laudantium</p>
  <div class="meta"><span><b>By :</b> Sed ut perspiciatis</span><span><b>0</b> Comments</span></div>
</article>

<!-- testimonials -->
<div class="abs testimonials"></div>
<h2 class="abs section-title" style="top:2574px">Client <span class="accent">Testimonials</span></h2>
<div class="abs rule" style="top:2628px"></div>
<div class="abs qmark" style="left:156px">&ldquo;</div>
<div class="abs qmark" style="left:990px">&rdquo;</div>
<p class="abs quote-text">Fusce elementum, nulla vel pellentes consequat, ante nulla hendrerit arcu, ac tincidunt mauris lacus sed leo. vamus suscipit molestie vestibulum. Lorem ipsum dolor sit amet, Fusce elementum, nulla vel pellentes consequat, ante nulla hendrerit arcu, ac tincidunt mauris lacus sed leo. vamus suscipit molestie. Fusce elementum, nulla vel</p>
<div class="abs client-name">Valerie</div>
<div class="photo avatar" style="left:437px;top:2796px;width:86px;height:86px;background:radial-gradient(circle,#c9a48a,#6b5a4c)" role="img" aria-label="Client portrait"></div>
<div class="photo avatar" style="left:553px;top:2791px;width:96px;height:96px;border:4px solid var(--green);background:radial-gradient(circle,#d8b8a0,#7f8a96)" role="img" aria-label="Client portrait of Valerie"></div>
<div class="photo avatar" style="left:679px;top:2796px;width:86px;height:86px;background:radial-gradient(circle,#d6ab8c,#5a3f33)" role="img" aria-label="Client portrait"></div>
<div class="abs dot" style="left:559px;background:var(--green)"></div>
<div class="abs dot" style="left:589px"></div>
<div class="abs dot" style="left:619px"></div>

<!-- footer -->
<footer class="abs footer">
  <h4 style="left:104px">Quick Links</h4>
  <ul style="left:104px"><li>Home</li><li>Meet Owen</li><li>Blog</li><li>Keynotes &amp; Speaking</li><li>Training &amp; Webinars</li><li>Coaching &amp; Consulting</li></ul>
  <ul style="left:303px"><li>Testimonials</li><li>Book Owen</li><li>Media Inquiries</li><li>Contact Us</li></ul>
  <div class="divider" style="left:482px"></div>
  <h4 style="left:569px">Contact Details</h4>
  <div class="contact-row" style="top:80px"><svg width="12" height="16" viewBox="0 0 12 16"><path d="M6 0a6 6 0 0 1 6 6c0 4-6 10-6 10S0 10 0 6a6 6 0 0 1 6-6z" fill="#fff"/><circle cx="6" cy="6" r="2" fill="#2d2d2d"/></svg><span>Lorem ipsum dolor sit consectetuer<br>adipiscing elit, diam nonummy nibh<br>Street No 5, zip Code: 897410</span></div>
  <div class="contact-row" style="top:140px"><svg width="12" height="14" viewBox="0 0 12 14"><path d="M2 0h3l1 4-2 1a8 8 0 0 0 3 4l1-2 4 1v3c0 1-1 2-2 2C5 13 0 8 0 2c0-1 1-2 2-2z" fill="#fff"/></svg><span>123-456-7890</span></div>
  <div class="contact-row" style="top:175px"><svg width="14" height="10" viewBox="0 0 14 10"><rect width="14" height="10" fill="#fff"/><path d="M0 0l7 6 7-6" fill="none" stroke="#2d2d2d" stroke-width="1.2"/></svg><span>info@owencastell-demo.net</span></div>
  <div class="divider" style="left:908px"></div>
  <h4 style="left:962px">Follow Us On</h4>
  <div class="follow-row" style="top:74px"><i></i>Facelink</div>
  <div class="follow-row" style="top:104px"><i></i>Chirper</div>
  <div class="follow-row" style="top:134px"><i></i>Globe+</div>
  <div class="follow-row" style="top:164px"><i></i>WorkNet</div>
</footer>
<div class="abs copyright">Copyright © 2016 Owen Castell. All Right Reserved.</div>

</body>
</html>
```